Cedar Lantern Steward Book Cover and Back Design

DESIGN BRIEF: The Cedar Lantern Steward Book Cover
Author: Mayor Calvin T. Ashby
Title: The Cedar Lantern Steward
Subtitle: Raising Stewards who shape neighborhoods
Genre: Leadership / Personal Development / Public Service
Format: Paperback + eBook + Hardcover
Design a visually compelling, iconic book cover that captures the essence of authentic, legacy-driven leadership using the metaphor of the mango tree. The cover should be vibrant, symbolic, and memorable—something that could stand alone as a brand and invite both credibility and curiosity.
Cover should NOT include:
Author’s face or personal photo
Overly busy visuals or political imagery
Literal images of mayors, buildings, or people
Cover SHOULD include:
A single iconic mango tree or mango fruit with visible deep roots
A vibrant and rich color palette—think mango orange, deep green, warm gold, and earth tones
A design that feels both modern and timeless, with symbolic depth
A sense of growth, depth, and legacy
Room for bold typography that pops in print and thumbnails
🖼️ VISUAL CONCEPT IDEAS
(Designer may interpret creatively, but these are preferred themes.)
A stylized mango tree with glowing mangoes and roots extending downward, set against a vibrant background (sunrise or rich green sky)
A mango fruit icon with leaves and roots subtly worked into the shape — could be used across brand platforms
Optional: Split background showing transformation — one side dry/cracked earth, the other lush and fruitful
Clean, modern layout with breathing space and balance between image and title
✍️ TYPOGRAPHY
Title Font: Strong, elegant serif or modern classic (e.g., Playfair Display, Garamond, or Libre Baskerville)
Subtitle Font: Clean and crisp sans serif (e.g., Lato, Montserrat)
Author Name: Bold, uppercase — not oversized, but clearly legible
🔠 COPY FOR COVER
Title:
The Cedar Lantern Steward
Subtitle:
Raising Stewards Who Shape Neighborhoods
Author Name:
Mayor Calvin T. Ashby
Optional Tagline or Teaser (for back or spine):
Stop performing like a politician. Start producing like a leader.
🔧 FORMAT DELIVERABLES
Front cover (paperback and hardcover versions)
Spine and back cover layout (with placeholder for barcode and description)
Web-optimized version for Veltrona SPX and other retailers
Square version for social media promotion
Optional: Icon version of tree or mango for branding
Back of book: Are you tired of leadership that looks impressive but produces no lasting fruit?
In a culture obsessed with image over integrity, quick wins over deep roots, and self-promotion over public service, we need a new kind of leader—one who leads for legacy, not likes.
What if you stopped leading like an apple tree—and started leading like a mango tree?
Apple trees grow fast and look good for a season, but their shallow roots can’t weather the storms. Mango trees grow slowly, but they last for generations—producing sweet, lasting fruit long after their planter is gone.
This isn’t just a metaphor. It’s a mindset shift. And it’s the key to leadership that actually transforms people, places, and policy.
Mayor Calvin Ashby has spent over a decade turning Dumfries, Virginia, from a town people drove through into a town people now drive to. Under his leadership:
• A former landfill became a half-billion-dollar resort
• A forgotten town rediscovered its purpose• A generation of young people began to see public service as purpose, not performance
In The Cedar Lantern Steward, you’ll discover how to:
✅ Lead from your authentic strengths—not trends or titles✅ Identify the unique problem you were born to solve✅ Build coalitions rooted in trust, not transaction✅ Make decisions that create sustainable change✅ Develop future leaders who multiply your impact✅ Leave a legacy that grows long after you’re gone
Whether you’re an elected official, aspiring public servant, nonprofit founder, or community-builder, this book will help you lead like a tree: planted deeply, growing steadily, and bearing fruit that feeds others for generations.
Stop performing like a politician. Start producing like a leader.Plant deep. Lead strong. Leave fruit that lasts.
By the time you finish this book, you won’t just understand the mango tree model—you’ll own it. You’ll walk away with clarity, courage, and a roadmap to become the kind of leader your community needs and your future demands.
Leadership

```html
<!DOCTYPE html>
<html lang="en">
<head>
<meta charset="utf-8">
<title>The Cedar Lantern Steward — Front Cover</title>
<link rel="stylesheet" href="https://fonts.googleapis.com/css2?family=Bebas+Neue&family=Oswald:wght@700&family=Playfair+Display:ital,wght@1,500&display=swap">
<style>
  :root {
    --page-bg: #ebe9e5;
    --cover-bg: #dfe6a8;
    --mango-orange: #e0641b;
    --ink: #0d0d0d;
    --leaf-deep: #3f9a2a;
    --leaf-light: #a9d34a;
    --fruit-gold: #f2b21e;
  }
  html, body {
    margin: 0;
    padding: 0;
    width: 1200px;
    height: 1200px;
    overflow: hidden;
    background: var(--page-bg);
  }
  .stage {
    width: 1200px;
    height: 1200px;
    display: flex;
    align-items: center;
    justify-content: center;
  }
  .book-cover {
    width: 736px;
    height: 1104px;
    display: block;
  }
  .cover-panel { fill: var(--cover-bg); }
  .title-article {
    font-family: "Playfair Display", serif;
    font-style: italic;
    font-weight: 500;
    font-size: 100px;
    fill: var(--ink);
  }
  .title-rule { fill: var(--ink); }
  .title-main {
    font-family: "Bebas Neue", sans-serif;
    font-size: 363px;
    fill: var(--mango-orange);
  }
  .title-secondary {
    font-family: "Bebas Neue", sans-serif;
    font-size: 197px;
    fill: var(--ink);
  }
  .subtitle {
    font-family: "Bebas Neue", sans-serif;
    font-size: 107px;
    fill: var(--mango-orange);
  }
  .author-name {
    font-family: "Oswald", sans-serif;
    font-weight: 700;
    font-size: 44px;
    fill: var(--ink);
  }
</style>
</head>
<body>
<main class="stage">
  <svg class="book-cover" viewBox="0 0 882 1324" xmlns="http://www.w3.org/2000/svg">
    <defs>
      <radialGradient id="tree-tones" cx="50%" cy="42%" r="60%">
        <stop offset="0%" stop-color="var(--fruit-gold)"/>
        <stop offset="45%" stop-color="var(--leaf-light)"/>
        <stop offset="100%" stop-color="var(--leaf-deep)"/>
      </radialGradient>
    </defs>

    <rect class="cover-panel" x="0" y="0" width="882" height="1324"/>

    <g class="title-block">
      <polygon class="title-rule" points="60,92 333,86 333,98"/>
      <polygon class="title-rule" points="548,86 823,92 548,98"/>
      <text class="title-article" x="441" y="124" text-anchor="middle">The</text>

      <text class="title-main" x="60" y="396" textLength="760" lengthAdjust="spacingAndGlyphs">CEDAR</text>
      <text class="title-secondary" x="60" y="552" textLength="765" lengthAdjust="spacingAndGlyphs">LANTERN STEWARD</text>

      <text class="subtitle" x="58" y="664" textLength="767" lengthAdjust="spacingAndGlyphs">RAISING STEWARDS WHO</text>
      <text class="subtitle" x="441" y="757" text-anchor="middle" textLength="730" lengthAdjust="spacingAndGlyphs">SHAPE NEIGHBORHOODS</text>
    </g>

    <rect class="cover-illustration" role="img" aria-label="Illustration of a fruit-laden tree with green leaves and golden-orange fruit standing on a small patch of grass"
          x="218" y="769" width="460" height="470" rx="200" fill="url(#tree-tones)"/>

    <text class="author-name" x="156" y="1299" textLength="587" lengthAdjust="spacing">MAYOR CALVIN T. ASHBY</text>
  </svg>
</main>
</body>
</html>
```